Corvin General Contracting

Roofing, Siding,windows, doors, Gutter,additions, decks, garagesand hanyman services fully insured and licensed, free estimates, accept all major credit cards call (614)392-7705 email corvinwr@mailbrook.net

Target Market(s)

Home improvement

Industry/Entity Type

Home Improvement

Requirements
Must have
• Whats listed above
Nice to have
• I dont have a logo i want wording for roofing, siding, gutter, decks, additions, windows, doors, and handyman services with my phone # 614-392-7705 and email corvinwr@mailbrook.net

```html
<!DOCTYPE html>
<html lang="en">
<head>
<meta charset="UTF-8">
<title>Corvin General Contracting – We've Got You Covered</title>
<link href="https://fonts.googleapis.com/css2?family=Montserrat:wght@500;700;800;900&display=swap" rel="stylesheet">
<style>
  :root {
    --brand-blue: #2e3192;
    --brand-red: #ed1c24;
    --ink-white: #ffffff;
  }
  html, body {
    margin: 0;
    padding: 0;
    overflow: hidden;
    background: var(--brand-blue);
  }
  .flyer {
    position: relative;
    width: 1200px;
    height: 930px;
    background: var(--brand-blue);
    color: var(--ink-white);
    font-family: "Montserrat", Arial, sans-serif;
    overflow: hidden;
  }
  .headline {
    position: absolute;
    left: 42px;
    top: 86px;
    margin: 0;
    font-weight: 800;
    font-size: 172px;
    line-height: 163px;
    letter-spacing: 0;
    text-transform: uppercase;
    white-space: nowrap;
  }
  .headline span { display: block; }
  .headline .accent { color: var(--brand-red); }
  .services {
    position: absolute;
    left: 57px;
    top: 611px;
    margin: 0;
    font-weight: 500;
    font-size: 26px;
    line-height: 49px;
    letter-spacing: 0.6px;
    white-space: nowrap;
  }
  .credentials {
    position: absolute;
    left: 56px;
    top: 742px;
    margin: 0;
    font-weight: 800;
    font-size: 18px;
    letter-spacing: 0.5px;
    text-transform: uppercase;
    white-space: nowrap;
  }
  .contact-bar {
    position: absolute;
    left: 0;
    right: 0;
    top: 842px;
    height: 44px;
  }
  .company-name {
    position: absolute;
    left: 56px;
    top: 50%;
    transform: translateY(-50%);
    font-weight: 800;
    font-size: 34px;
    letter-spacing: 0.3px;
    white-space: nowrap;
  }
  .contact-item {
    position: absolute;
    top: 0;
    height: 44px;
    display: flex;
    align-items: center;
    gap: 5px;
    font-weight: 700;
    font-size: 21px;
    letter-spacing: 0.2px;
    color: var(--ink-white);
    text-decoration: none;
    white-space: nowrap;
  }
  .contact-item.phone { left: 597px; }
  .contact-item.email { left: 855px; }
  .contact-icon { width: 44px; height: 44px; flex: none; }
</style>
</head>
<body>
  <main class="flyer">
    <h1 class="headline">
      <span>We’ve</span>
      <span>Got You</span>
      <span class="accent">Covered</span>
    </h1>

    <p class="services">
      Whether Roofing, Siding, Windows, Doors, Gutter, Additions,<br>
      Decks or Garages, Our Handyman Services Will Take Care of It.
    </p>

    <p class="credentials">Fully Insured and Licensed • Free Estimates • All Major Credit Cards Accepted</p>

    <footer class="contact-bar">
      <span class="company-name">Corvin General Contracting</span>

      <a class="contact-item phone" href="tel:6143927705">
        <svg class="contact-icon" viewBox="0 0 44 44" aria-hidden="true">
          <circle cx="22" cy="22" r="20" fill="none" stroke="#fff" stroke-width="2.5"/>
          <path d="M15.5 11.5c1-.8 2.2-.6 2.9.4l2.3 3.4c.6.9.4 2-.4 2.7l-1.4 1.1c.9 2.2 2.7 4.2 4.9 5.3l1.2-1.4c.7-.8 1.9-.9 2.7-.3l3.4 2.4c1 .7 1.1 2 .3 2.9l-1.6 1.8c-1 1.1-2.6 1.5-4 1-6.3-2.1-10.9-7.1-12.6-13.4-.4-1.4.1-2.9 1.2-3.8z" fill="#fff"/>
        </svg>
        <span>(614)392-7705</span>
      </a>

      <a class="contact-item email" href="mailto:corvinwr@mailbrook.net">
        <svg class="contact-icon" viewBox="0 0 44 44" aria-hidden="true">
          <circle cx="22" cy="22" r="20" fill="none" stroke="#fff" stroke-width="2.5"/>
          <rect x="12" y="15" width="20" height="14" rx="1" fill="#fff"/>
          <path d="M12.5 15.5 22 23l9.5-7.5M12.5 28.5l7-6M31.5 28.5l-7-6" fill="none" stroke="var(--brand-blue)" stroke-width="1.4"/>
        </svg>
        <span>corvinwr@mailbrook.net</span>
      </a>
    </footer>
  </main>
</body>
</html>
```